"Folvo Package Design"

We are looking to develop a standard package for our new range of frozen bakery products. As you can imagine any frozen product itself is not very appeling when looking at it so we want to showcase on our package the product after being made. We are looking to a package that really makes the people wanna try to bake our products.

We need a similar package design for all our products, the only thing that will change is the image of the product according to the range of product.

The products will vary between three ranges:

Bread ( Baguettes, bread rolls, etc)
American products (donuts, muffins and brownies)
Pastry ( Croissants, belgian butter pastries )

We dont want different package design for each of them, the only thing we may change for each one is the colour pallete, and of course the image of the product.

Nutritional information and Preparation guidelines need to be in the package too. They are not defined yet so please use a sample one.

Modern packaging needs to contain, protect, preserve, transport, inform and sell. It needs to be clever, attractive, sustainable and innovative. And thats the principles of our brand.

Stock Photography can be used as an example.
Updates

Package measurements: Lenght 25cm - Deep 17cm - High - 8cm

We need a see thru top in each package in order to see the product inside. At least half of the top cover needs to be see thru.

Thank you

We need a see-thru front on this package. Maybe at least half of the top front side that we could see the product inside.

Thank you

Target Market(s)

Young crowd and mum's

Industry/Entity Type

Bakery

Requirements
Must have
• Product Photography
Product Logo
Nutritional Information
Preparation Guidelines
Product name
Product Description

```html
<!DOCTYPE html>
<html lang="en">
<head>
<meta charset="utf-8">
<title>Folvo Package Design</title>
<link rel="stylesheet" href="https://fonts.googleapis.com/css2?family=Cinzel:wght@700&family=Comfortaa:wght@700&family=Lobster&display=swap">
<style>
  :root {
    --bg: #ffffff;
    --box: #fbfbfb;
    --end: #f1f1f1;
    --box-edge: #e4e4e4;
    --brown: #5a3a22;
    --gold: #e39b2c;
    --gold-line: #f0b55a;
    --donut: #d66fa8;
    --donut-soft: #e6a0c8;
    --bread: #c21f4c;
    --pastry: #f2a623;
    --tag-brown: #5b3a1e;
  }
  * { box-sizing: border-box; margin: 0; padding: 0; }
  html, body { width: 1200px; height: 742px; overflow: hidden; background: var(--bg); }
  .canvas { position: relative; width: 1200px; height: 742px; }

  .pack {
    position: absolute;
    width: 710px; height: 218px;
    display: flex;
    box-shadow: 0 8px 16px rgba(0,0,0,0.10);
  }
  .pack--donuts { left: 82px; top: 105px; --accent: var(--donut); --ribbon: var(--donut-soft); --tag: var(--donut); }
  .pack--baguettes { left: 255px; top: 267px; --accent: var(--bread); --ribbon: var(--bread); --tag: var(--bread); }
  .pack--croissants { left: 427px; top: 428px; --accent: var(--pastry); --ribbon: var(--pastry); --tag: var(--tag-brown); }

  .pack__end {
    width: 60px; height: 100%;
    background: var(--end);
    border: 1px solid var(--box-edge);
    border-right: none;
    display: flex; flex-direction: column; align-items: center;
    padding-top: 18px; gap: 6px;
  }
  .pack__end-mark { width: 14px; height: 14px; border-radius: 50%; background: var(--brown); }
  .pack__end-name {
    font-family: 'Lobster', cursive; font-size: 13px; color: var(--brown);
    writing-mode: vertical-rl;
  }

  .pack__front {
    position: relative;
    width: 650px; height: 100%;
    background: var(--box);
    border: 1px solid var(--box-edge);
    overflow: hidden;
  }

  .window {
    position: absolute; left: 18px; top: 34px;
    width: 282px; height: 150px;
    border-radius: 75px;
    border: 7px solid var(--accent);
    overflow: hidden;
  }
  .window__product { width: 100%; height: 100%; }
  .pack--donuts .window__product { background: radial-gradient(ellipse at 35% 50%, #f3dcc4, #d9b48c 60%, #c89a6e); }
  .pack--baguettes .window__product { background: linear-gradient(160deg, #e9ddd0, #b8916a 45%, #d9c6b2 70%, #a77c55); }
  .pack--croissants .window__product { background: linear-gradient(170deg, #e8d8c6, #c09063 45%, #a87545 70%, #dcc6ae); }

  .brand {
    position: absolute; left: 312px; top: 14px; width: 200px;
    display: flex; align-items: center; justify-content: center; gap: 6px;
  }
  .brand__mark { width: 14px; height: 14px; border-radius: 50%; background: var(--brown); }
  .brand__name { font-family: 'Lobster', cursive; font-size: 21px; color: var(--brown); }

  .label {
    position: absolute; left: 312px; top: 66px; width: 200px;
    text-align: center;
    border-top: 2px solid var(--gold-line);
    border-bottom: 2px solid var(--gold-line);
    padding: 7px 0 5px;
  }
  .label__name {
    font-family: 'Cinzel', serif; font-weight: 700;
    font-size: 24px; line-height: 1; color: var(--brown);
    white-space: nowrap;
  }
  .label__name span { font-size: 32px; }
  .label__line {
    font-family: 'Comfortaa', sans-serif; font-weight: 700;
    font-size: 11px; color: var(--gold); letter-spacing: 1px; margin-top: 4px;
    white-space: nowrap;
  }

  .tag {
    position: absolute; left: 362px; top: 146px; width: 100px;
    padding: 4px 0; text-align: center;
    background: var(--tag); color: #fff;
    font-family: 'Comfortaa', sans-serif; font-weight: 700; font-size: 10px;
  }

  .hero {
    position: absolute; left: 526px; top: 52px; width: 118px; height: 160px;
    border-radius: 36px;
  }
  .pack--donuts .hero { background: linear-gradient(180deg, #6b3a24 0%, #e0a866 35%, #f2c07a 60%, #e57aa8 88%); }
  .pack--baguettes .hero { background: linear-gradient(165deg, #e7a85a, #d08838 50%, #f0c27e); }
  .pack--croissants .hero { background: radial-gradient(ellipse at 50% 55%, #e9a34c, #c87a2a 60%, #f6e3c9 95%); }

  .ribbon { position: absolute; right: 0; top: 0; width: 60px; height: 60px; }
  .ribbon__text {
    position: absolute; right: 4px; top: 7px; width: 40px;
    font-family: 'Comfortaa', sans-serif; font-weight: 700; font-size: 9px;
    line-height: 1.15; color: #fff; text-align: center;
  }
  .count {
    position: absolute; right: 10px; bottom: 12px;
    width: 20px; height: 20px; background: var(--pastry);
    color: #fff; font-family: 'Comfortaa', sans-serif; font-weight: 700; font-size: 12px;
    display: flex; align-items: center; justify-content: center;
  }
</style>
</head>
<body>
<main class="canvas">

  <section class="pack pack--donuts">
    <div class="pack__end"><span class="pack__end-mark"></span><span class="pack__end-name">Folvo</span></div>
    <div class="pack__front">
      <div class="window"><div class="window__product" role="img" aria-label="Frozen glazed donuts seen through the clear window"></div></div>
      <div class="brand"><span class="brand__mark"></span><span class="brand__name">Folvo</span></div>
      <div class="label">
        <h2 class="label__name"><span>D</span>ONUTS</h2>
        <p class="label__line">· American products ·</p>
      </div>
      <div class="tag">Ready to bake</div>
      <div class="hero" role="img" aria-label="Photo of stacked chocolate and pink glazed donuts"></div>
      <svg class="ribbon" viewBox="0 0 60 60"><polygon points="0,0 60,0 60,60" fill="var(--ribbon)"/></svg>
      <p class="ribbon__text">keep frozen</p>
    </div>
  </section>

  <section class="pack pack--baguettes">
    <div class="pack__end"><span class="pack__end-mark"></span><span class="pack__end-name">Folvo</span></div>
    <div class="pack__front">
      <div class="window"><div class="window__product" role="img" aria-label="Frozen baguettes seen through the clear window"></div></div>
      <div class="brand"><span class="brand__mark"></span><span class="brand__name">Folvo</span></div>
      <div class="label">
        <h2 class="label__name"><span>B</span>AGUETTES</h2>
        <p class="label__line">· Bread Specialities ·</p>
      </div>
      <div class="tag">Ready to bake</div>
      <div class="hero" role="img" aria-label="Photo of freshly baked golden baguettes"></div>
      <svg class="ribbon" viewBox="0 0 60 60"><polygon points="0,0 60,0 60,60" fill="var(--ribbon)"/></svg>
      <p class="ribbon__text">keep frozen</p>
    </div>
  </section>

  <section class="pack pack--croissants">
    <div class="pack__end"><span class="pack__end-mark"></span><span class="pack__end-name">Folvo</span></div>
    <div class="pack__front">
      <div class="window"><div class="window__product" role="img" aria-label="Frozen croissants seen through the clear window"></div></div>
      <div class="brand"><span class="brand__mark"></span><span class="brand__name">Folvo</span></div>
      <div class="label">
        <h2 class="label__name"><span>C</span>ROISSANTS</h2>
        <p class="label__line">· Pastry Specialities ·</p>
      </div>
      <div class="tag">Ready to bake</div>
      <div class="hero" role="img" aria-label="Photo of freshly baked butter croissants"></div>
      <svg class="ribbon" viewBox="0 0 60 60"><polygon points="0,0 60,0 60,60" fill="var(--ribbon)"/></svg>
      <p class="ribbon__text">keep frozen</p>
      <div class="count">6</div>
    </div>
  </section>

</main>
</body>
</html>
```